New webdesign for a cable company

We need a new design for Lumo Nett.

There exist a suggestion for the page, were we have attached files to show you this. The design here is not good enough, but here you can se what content we need.

You can feel free to give adjustment to this design to make it better, our blow us away with a new brilliant design, but from this design you see what content we need.

The important is that the company get a design who represent its products:
- TV = Cable TV
- Bredbånd = Broadband
- Mobil = Mobile phone
- Strøm = Electricity
- Alarm = Alarm
- Lumo Samlet = a cobain pagage of all our products.

Lumo Nett would like costumers who visit the site to het the impression that Lumo Nett is a professional, innovative and fun company.
Updates

We have to day uploaded pictures of the existing page as the link haven't been working for the most of you as it's placed on a server our developer are using and is often shut it down. 

We have also updated the brief with some new and updated description so please read true the updated brief. 

We will at the same time inform that we haven't been able to give feedback on any of the received design and are sorry for that, we will within the next 24 hours hopefully have started responded the different received designs.

Looking forward to see more suggestion and hope you will help us create and very professional and informative design. 

Reason: We have decided to extend the deadline due to the number of design suggestion who is sent in and your lack of response to all designers due to our own workload.

This project was unfortunately for different reason put on ice for a while, but we are now ready to complete the design and will answer and give feedback too all the received design suggestions. 

Within a couple of days we hope we have answered all you who sent us suggestions, we appreciate all suggestions and hope to get in more suggestions.

Reason: Deisgn description have been updated

Target Market(s)

Our costumer are both private and companies

Industry/Entity Type

Tv

Requirements
Must have
• A easy way to promote and inform about changes in our products, there are a constant change in our products and it must bee a easy and good way to changes ass the marked change. Cheek out this link, for a example of what we like/think of here, https://kabel.fjordvisjon.no

On all pages there must be a easy way to click on a order button and too inform about your interest (thats two different things), could be placed in the top right corner for example. In the order form you should follow a step by step part:
1. Cheek what product we can provide you.
2. Chooce products.
3. Costumer inforamtion.
4. Confirmation.

Somewere on the portal it must be possible for costumers to log on to their own administration, where they can cheek for invoices, other statuses, etc.

A main menu existing of:
Hjem (Home)
Produkter (Products)
Storkunde (key account/large costumers)
Kundeservice (Costumerservice)
Min side (My page)

The main menu should have the following sub titles:
- Under "Produkter"/products our different products must be listed
- Under "Kundeservice"/Costumerservice it must have these submenus:
- Hjelp og støtte = Help.
- Faktura = Invoice
- Brukerguider = Userguides
- Abbonementavtaler = Terms and conditions.

A bottom menu where we have 5 main categories, with sub categories:
Om oss (about us)
- Om Lumo Nett (about Lumo Nett)
- Kontaktinformajson ( contact information)
- Pressemeldinger (Pressrelese)
- Ledige stillinger (positions available)
- KRAB ( and organisastion in our field)

Produkter (Product)
- TV (TV)
- Bredbånd (Broadand)
- Telefoni (telephony, both mobil)
- Strøm (elecricity)
- Arlam (Alarm)

Borrettslag/Sameier (Housing cooperatives)
- Løsninger (solutions)
- Produkter (product)
- Kontaktpersoner (contactpersons)

Utbygger (developer)
- Hva vi kan gjøre for dere. (What we can do for you)

Opperatørnett (operators)

Build up the categories and bottom menu something like this:
https://kabel.fjordvisjon.no
www.brenvik.com
Nice to have
• A main menu existing of:
Hjem (Home)
Produkter (Products)
Lumo Nett
Kontakt oss (Contact us)

Under "Produkter"/products our different products must be listed and under "Kundeservice"/Costumerservice it must have these submenus:
- Hjelp og støtte = Help.
- Faktura = Invoice
Should not have
• Any translation section since the homepage only will be in Norwegian.

```html
<!DOCTYPE html>
<html lang="no">
<head>
<meta charset="utf-8">
<title>Lumo Nett – Hjem</title>
<link rel="stylesheet" href="https://fonts.googleapis.com/css2?family=Cabin:wght@400;600&family=Didact+Gothic&display=swap">
<style>
:root{
  --blue:#2cb8ea;
  --blue-text:#35aee0;
  --dark:#4a4a4a;
  --ink:#111;
  --grey-text:#6b6b6b;
  --light-grey:#b8b8b8;
  --footer-bg:#ecedee;
  --line:#d3d4d6;
  --white:#fff;
}
*{box-sizing:border-box;margin:0;padding:0}
html,body{width:960px;height:1200px;overflow:hidden;background:var(--white)}
body{position:relative;font-family:"Cabin",sans-serif;color:var(--grey-text)}
.abs{position:absolute}

.device-tab{left:234px;top:0;width:488px;height:34px}
.brand{left:19px;top:52px;display:flex;align-items:center;gap:14px}
.brand-dot{width:46px;height:46px;border-radius:50%;background:var(--blue)}
.brand-name{font-family:"Didact Gothic",sans-serif;font-size:45px;color:var(--blue);line-height:1}

.util-links{left:842px;top:12px;font-family:Arial,sans-serif;font-size:13px;line-height:22px;color:var(--light-grey)}
.util-links .translate{color:#333;font-size:12px;margin-left:24px}

.main-nav{left:0;top:141px;width:960px;height:37px;background:var(--dark);font-family:"Didact Gothic",sans-serif;font-size:22.5px;color:var(--white)}
.main-nav span{position:absolute;top:0;line-height:37px;white-space:nowrap}
.main-nav .active{left:19px;width:81px;background:var(--blue);text-align:center}

.hero{left:0;top:181px;width:960px;height:473px}
.hero-photo{left:0;top:181px;width:960px;height:473px}
.hero-title{left:680px;top:232px;font-family:"Didact Gothic",sans-serif;font-weight:400;font-size:42px;color:var(--ink);word-spacing:8px}
.hero-line{left:595px;width:350px;font-size:21px;line-height:27px;color:var(--white)}
.hero-line.bold{font-family:Arial,sans-serif;font-weight:bold;font-size:17px}
.hero-line.small{font-size:17.5px}
.more-btn{left:714px;top:578px;width:169px;height:42px;border-radius:5px;background:linear-gradient(#fafafa,#dcdcdc);display:flex;align-items:center;justify-content:center;gap:10px;font-family:"Didact Gothic",sans-serif;font-size:29px;color:var(--ink)}
.more-btn .hl{color:var(--blue)}

.shortcuts{left:19px;top:684px;width:921px;height:151px;border:2px solid #e2e3e4;border-radius:10px;display:flex}
.shortcut{flex:none;position:relative;display:flex;flex-direction:column;align-items:center;justify-content:flex-end;padding-bottom:12px;border-right:2px dashed #e6e6e6;color:var(--blue-text);font-size:18px}
.shortcut:last-child{border-right:none}
.shortcut svg,.shortcut .art{position:absolute;top:14px}
.art{border-radius:6px}

.footer{left:0;top:877px;width:960px;height:323px;background:var(--footer-bg);border-top:2px solid #dddfe0;border-radius:8px 8px 0 0}
.links-tag{left:14px;top:963px;font-size:19px;color:var(--blue);line-height:27.5px;text-align:center;width:12px}
.col{top:902px;font-size:18px;line-height:22.5px;color:var(--grey-text)}
.col-a{left:58px}.col-b{left:247px}
.divider{top:878px;width:0;height:322px;border-left:2px dashed var(--line)}
.hours{left:506px;top:967px;font-size:18px}
.phone{left:530px;top:1012px;font-size:41px;line-height:50px}
.mail{left:493px;top:1090px;font-size:18px}
.mail a{color:var(--blue-text);text-decoration:none}
</style>
</head>
<body>

<div class="abs device-tab" role="img" aria-label="Product icons: router, mobile, electricity, TV, alarm box">
  <svg width="488" height="34" viewBox="0 0 488 34">
    <polygon points="0,0 488,0 462,34 26,34" fill="#555"/>
    <rect x="118" y="10" width="38" height="14" rx="2" fill="#ececec"/>
    <rect x="184" y="4" width="18" height="26" rx="2" fill="#ececec"/>
    <polygon points="240,2 228,18 238,18 232,32 248,13 238,13 246,2" fill="#ececec"/>
    <rect x="258" y="5" width="42" height="24" rx="1" fill="#ececec"/>
    <rect x="330" y="6" width="34" height="24" rx="3" fill="#ececec"/>
  </svg>
</div>

<div class="abs brand">
  <div class="brand-dot"></div>
  <div class="brand-name">Lumo Nett</div>
</div>

<div class="abs util-links">
  <div class="translate">Translate Page</div>
  <div style="margin-top:6px">Kontaktinformasjon</div>
  <div>Pressemeldinger</div>
  <div>Ledige stillinger</div>
</div>

<nav class="abs main-nav">
  <span class="active">Hjem</span>
  <span style="left:118px">Om oss</span>
  <span style="left:215px">Om Lumo Nett</span>
  <span style="left:404px">Produkter</span>
  <span style="left:531px">Storkunde</span>
  <span style="left:662px">Kundeservice</span>
  <span style="left:829px">Min side</span>
</nav>

<div class="abs hero-photo" role="img" aria-label="Photo of a man relaxing with hands behind his head in front of a television" style="background:linear-gradient(160deg,#3a3d44 0%,#6f7f9c 35%,#c8ccd2 65%,#e8e8e8 100%)"></div>
<svg class="abs hero" width="960" height="473" viewBox="0 0 960 473">
  <polygon points="670,0 960,0 960,473 675,473 422,231" fill="var(--blue)"/>
</svg>
<h1 class="abs hero-title">Lumo TV</h1>
<p class="abs hero-line" style="top:307px">Vare TV kunder has mye gelede seg over.</p>
<p class="abs hero-line" style="top:365px">Musikktjeneste og filmlete pa TV en</p>
<p class="abs hero-line" style="top:400px">15 valgfrie kanaler</p>
<p class="abs hero-line bold" style="top:440px">TV i flere rom kr .0,-*</p>
<p class="abs hero-line small" style="top:474px">Rikt utalg av ekstrakanaler</p>
<div class="abs more-btn"><span><span class="hl">Vid</span>ere</span>
  <svg width="20" height="30" viewBox="0 0 20 30"><polyline points="4,3 16,15 4,27" fill="none" stroke="var(--blue)" stroke-width="5"/></svg>
</div>

<div class="abs shortcuts">
  <div class="shortcut" style="width:191px">
    <svg width="92" height="92" viewBox="0 0 92 92"><circle cx="46" cy="28" r="22" fill="none" stroke="#111" stroke-width="6"/><path d="M3,90 Q3,56 46,56 Q89,56 89,90 Z" fill="none" stroke="#111" stroke-width="6"/></svg>
    Kontaktpersoner</div>
  <div class="shortcut" style="width:196px">
    <div class="art" role="img" aria-label="Illustration of a screwdriver and wrench" style="width:100px;height:96px;background:linear-gradient(135deg,#f3b21a,#9aa1a8)"></div>
    Løsninger</div>
  <div class="shortcut" style="width:199px">
    <div class="art" role="img" aria-label="Illustration of an invoice with a pen" style="width:110px;height:100px;background:linear-gradient(135deg,#f4f4f4,#bfc2c6)"></div>
    Faktura</div>
  <div class="shortcut" style="width:209px">
    <svg width="146" height="84" viewBox="0 0 146 84"><polygon points="73,0 0,44 14,44 14,84 132,84 132,44 146,44" fill="#111"/><rect x="62" y="50" width="22" height="22" fill="#fff"/></svg>
    Borrettslag/Sameier</div>
  <div class="shortcut" style="width:122px">
    <div class="art" style="top:4px;font-family:Arial,sans-serif;font-weight:bold;font-size:104px;color:#111;line-height:1">?</div>
    Hjelp og støtte</div>
</div>

<div class="abs footer"></div>
<div class="abs divider" style="left:42px"></div>
<div class="abs divider" style="left:229px"></div>
<div class="abs divider" style="left:429px"></div>
<div class="abs links-tag">L I N K S</div>
<div class="abs col col-a">
  Hejm<br>Omoss<br>Om Lumo Nett<br>produkter<br>storkunde<br>khundeservice<br>min side<br>Kontaktpersoner<br>Løsninger<br>Faktura<br>Borrettslag/Sameier<br>Hjelp og støtte<br>Utbygger
</div>
<div class="abs col col-b">
  Brukerguider<br>Abbonementavtaler<br>TV<br>Bredbånd<br>Telefoni<br>Strøm<br>Arlam<br>Kontaktinformasjon<br>Pressemeldinger<br>Ledige stillinger<br>KRAB<br>Borrettslag/Sameier<br>Opperatørnett
</div>
<div class="abs hours">Ring oss hverdager 10:00 - 15:00</div>
<div class="abs phone">41 58 20 37</div>
<div class="abs mail">Eller send e-post pa : <a href="mailto:post@lumonett.no">post@lumonett.no</a></div>

</body>
</html>
```